Medical clinic VALORENT sales materials presentation folder

I am looking for a professional design to a sales/presentation folder for VALORENT medical clinic. I would like to get picture of doctor in a class design.
I had an example of a hold marketing and the VALORENT LOGO.
VALORENT have 5 clinics and we are serious whit lot of doctors. We are doing lot of medical service. I put a doctor picture, but if you have a better choice for the presentation folder don't hesitate to use it.

Target Market(s)

Medical customer and corporation

Industry/Entity Type

Health care

Requirements
Must have
• Professional design - red accent
Nice to have
• Medical doctor picture
Should not have
• Don't want the same hold design that the example

```html
<!DOCTYPE html>
<html lang="en">
<head>
<meta charset="utf-8">
<title>VALORENT presentation folder</title>
<link rel="stylesheet" href="https://fonts.googleapis.com/css2?family=Poppins:wght@400;500;600;700;800&display=swap">
<style>
  :root {
    --backdrop: #ff6b6b;
    --brand-red: #e21e2d;
    --brand-red-deep: #d31b29;
    --accent-orange: #e8702a;
    --ink: #1f1f1f;
    --paper: #ffffff;
    --photo-light: #f7f7f7;
    --photo-coat: #e9e9ea;
    --photo-hair: #4a4442;
    --photo-skin: #c99a80;
  }
  html, body {
    margin: 0;
    padding: 0;
    width: 1200px;
    height: 1200px;
    overflow: hidden;
    background: var(--backdrop);
  }
  .folder {
    display: block;
    width: 1200px;
    height: 1200px;
    font-family: "Poppins", sans-serif;
  }
  .flap, .pocket { fill: var(--paper); }
  .cover { fill: var(--brand-red); }
  .cover-facet { fill: var(--brand-red-deep); }
  .photo-edge { fill: none; stroke: var(--accent-orange); stroke-width: 4; }
  .corner-name { fill: var(--brand-red); font-weight: 700; font-size: 24px; letter-spacing: 1px; }
  .headline { fill: var(--ink); font-weight: 800; font-size: 94px; letter-spacing: -2px; }
  .headline-mark { fill: var(--paper); }
  .tagline-bar { fill: var(--ink); }
  .tagline { fill: var(--paper); font-weight: 500; font-size: 24px; }
  .cta-button { fill: var(--ink); }
  .cta-label { fill: var(--paper); font-weight: 600; font-size: 31px; }
  .icon-rail { fill: var(--ink); }
  .icon-disc { fill: var(--ink); stroke: var(--paper); stroke-width: 2; }
  .icon-glyph { fill: none; stroke: var(--paper); stroke-width: 1.8; stroke-linecap: round; stroke-linejoin: round; }
  .contact-phone { fill: var(--paper); font-size: 25px; letter-spacing: 6px; }
  .contact-email { fill: var(--paper); font-size: 26px; }
  .contact-address { fill: var(--paper); font-size: 19px; }
  .pocket-name { fill: var(--ink); font-weight: 700; font-size: 34px; }
  .pocket-mark { fill: var(--brand-red); }
</style>
</head>
<body>
<svg class="folder" viewBox="0 0 1200 1200" xmlns="http://www.w3.org/2000/svg">
  <defs>
    <radialGradient id="photo-tone" cx="0.42" cy="0.45" r="0.62">
      <stop offset="0" stop-color="var(--photo-skin)" stop-opacity="0.55"/>
      <stop offset="0.28" stop-color="var(--photo-hair)" stop-opacity="0.45"/>
      <stop offset="0.62" stop-color="var(--photo-coat)"/>
      <stop offset="1" stop-color="var(--photo-light)"/>
    </radialGradient>
  </defs>

  <!-- side flap -->
  <polygon class="flap" points="38,596 98,590 98,826 38,798"/>

  <!-- bottom pocket -->
  <path class="pocket" d="M98,831 H630 L612,1031 Q600,1084 553,1084 H128 Q101,1084 101,1057 Z"/>
  <g transform="rotate(180 360 975)">
    <rect class="pocket-mark" x="223" y="941" width="68" height="68"/>
    <text class="pocket-name" x="305" y="987">VALORENT</text>
  </g>

  <!-- front cover -->
  <path class="cover" d="M98,116 H1137 Q1162,116 1162,141 V806 Q1162,831 1137,831 H98 Z"/>
  <polygon class="cover-facet" points="760,116 1162,116 1162,300 980,116"/>
  <polygon class="cover-facet" points="1005,135 1162,290 1162,340 1005,340"/>
  <polygon class="cover-facet" points="1162,370 1080,370 1162,450"/>
  <polygon class="cover-facet" points="1100,495 1162,555 1162,597 995,597"/>
  <polygon class="cover-facet" points="98,660 260,831 98,831"/>
  <polygon class="cover-facet" points="780,831 900,720 980,831"/>

  <!-- doctor photograph area -->
  <polygon role="img" aria-label="Photo of a smiling doctor in a white coat with a red stethoscope, writing on a clipboard"
           fill="url(#photo-tone)" points="99,118 686,118 913,366 447,826 286,826 99,643"/>
  <polyline class="photo-edge" points="688,116 915,366 449,828"/>
  <polyline class="photo-edge" points="98,643 284,828"/>

  <text class="corner-name" x="138" y="207">VALORENT</text>

  <!-- headline name -->
  <rect class="headline-mark" x="684" y="222" width="62" height="62"/>
  <text class="headline" x="758" y="286">VALO</text>
  <text class="headline" x="680" y="366">RENT</text>

  <rect class="tagline-bar" x="684" y="383" width="444" height="40"/>
  <text class="tagline" x="695" y="412">LE BON CHOIX - THE RIGHT CHOICE</text>

  <!-- contact -->
  <rect class="cta-button" x="763" y="528" width="272" height="52" rx="12"/>
  <text class="cta-label" x="899" y="565" text-anchor="middle">CONTACT US</text>

  <rect class="icon-rail" x="725" y="640" width="20" height="86"/>
  <circle class="icon-disc" cx="735" cy="641" r="17"/>
  <circle class="icon-disc" cx="735" cy="684" r="17"/>
  <circle class="icon-disc" cx="735" cy="726" r="17"/>
  <path class="icon-glyph" d="M729,633 h11 v16 h-11 z M732,637 q1,6 6,8"/>
  <path class="icon-glyph" d="M727,679 h16 v11 h-16 z M727,679 l8,6 l8,-6"/>
  <path class="icon-glyph" d="M735,733 q-6,-6 -6,-11 a6,6 0 0 1 12,0 q0,5 -6,11 z M731,735 h8"/>

  <text class="contact-phone" x="781" y="651">555 014-2730</text>
  <text class="contact-email" x="781" y="693">info@valorentsante.com</text>
  <text class="contact-address" x="781" y="733">120, rue des ormes, local 305</text>
  <text class="contact-address" x="781" y="757">Lacville(Quebec) H0H 1B2</text>
</svg>
</body>
</html>
```